Quarlwick Builders Business Cards

I want to use the logo and make an unique business card that shows the textured Logo with brick and builings. I want to be able to stand out when I pass out business cards.

```html
<!DOCTYPE html>
<html lang="en">
<head>
<meta charset="utf-8">
<title>Quarlwick Builders Business Cards</title>
<link rel="stylesheet" href="https://fonts.googleapis.com/css2?family=Tinos:wght@400;700&display=swap">
<style>
  :root {
    --backdrop: #3a3a3a;
    --card: #050505;
    --accent: #e4491d;
    --ink: #f4f1ee;
    --ghost: rgba(228, 73, 29, 0.13);
  }
  * { margin: 0; padding: 0; box-sizing: border-box; }
  html, body { width: 1200px; height: 694px; overflow: hidden; }
  body {
    background: var(--backdrop);
    font-family: "Tinos", "Times New Roman", serif;
    color: var(--ink);
    position: relative;
  }
  .card {
    position: absolute;
    top: 193px;
    width: 540px;
    height: 308px;
    background: var(--card);
    border-radius: 22px;
    overflow: hidden;
  }
  .card--front { left: 40px; }
  .card--back { left: 620px; }

  .brand-mark {
    display: flex;
    align-items: center;
    gap: 12px;
    color: var(--accent);
    font-weight: 700;
  }
  .brand-mark__square {
    width: 18px; height: 18px; background: var(--accent);
  }
  .card--front .brand-mark {
    position: absolute;
    top: 50%; left: 50%;
    transform: translate(-50%, -50%);
    font-size: 40px;
    letter-spacing: 1px;
    white-space: nowrap;
  }

  .brand-ghost {
    position: absolute;
    right: 30px; top: 76px;
    font-size: 40px;
    font-weight: 700;
    color: var(--ghost);
    text-align: right;
    white-space: nowrap;
    line-height: 1.05;
  }
  .card--back .brand-mark {
    position: absolute;
    top: 30px; right: 36px;
    font-size: 22px;
    white-space: nowrap;
  }

  .holder {
    position: absolute;
    left: 0; top: 96px;
    padding-left: 34px;
    border-left: 6px solid var(--accent);
    margin-left: 22px;
  }
  .holder__name { font-size: 28px; font-weight: 700; color: var(--accent); line-height: 1.1; white-space: nowrap; }
  .holder__role { font-size: 17px; margin-top: 4px; }

  .contacts {
    position: absolute;
    left: 56px; bottom: 34px;
    list-style: none;
    font-size: 17px;
    line-height: 1.55;
  }
  .contacts li, .address { display: flex; align-items: center; gap: 12px; }
  .icon { width: 16px; height: 16px; fill: var(--accent); flex: none; }

  .address {
    position: absolute;
    right: 34px; top: 178px;
    font-size: 16px;
    line-height: 1.35;
  }
</style>
</head>
<body>
  <section class="card card--front" aria-label="Card front">
    <div class="brand-mark">
      <span class="brand-mark__square"></span>
      <span>Quarlwick Builders</span>
    </div>
  </section>

  <section class="card card--back" aria-label="Card back">
    <div class="brand-ghost" aria-hidden="true">Quarlwick<br>Builders</div>

    <div class="brand-mark">
      <span class="brand-mark__square"></span>
      <span>Quarlwick Builders</span>
    </div>

    <div class="holder">
      <p class="holder__name">Dorian Pellwright</p>
      <p class="holder__role">Owner</p>
    </div>

    <ul class="contacts">
      <li>
        <svg class="icon" viewBox="0 0 24 24" aria-hidden="true"><path d="M6.6 10.8a15 15 0 0 0 6.6 6.6l2.2-2.2c.3-.3.7-.4 1-.2 1.1.4 2.3.6 3.6.6.6 0 1 .4 1 1V20c0 .6-.4 1-1 1A17 17 0 0 1 3 4c0-.6.4-1 1-1h3.5c.6 0 1 .4 1 1 0 1.3.2 2.5.6 3.6.1.3 0 .7-.2 1z"/></svg>
        <span>123.456.7890</span>
      </li>
      <li>
        <svg class="icon" viewBox="0 0 24 24" aria-hidden="true"><path d="M2 5h20v14H2z"/><path d="M3 6l9 7 9-7" fill="none" stroke="#050505" stroke-width="1.6"/></svg>
        <span>info@webname.com</span>
      </li>
      <li>
        <svg class="icon" viewBox="0 0 24 24" aria-hidden="true"><circle cx="12" cy="12" r="10"/><path d="M2 12h20M12 2c3 3 3 17 0 20M12 2c-3 3-3 17 0 20" fill="none" stroke="#050505" stroke-width="1.4"/></svg>
        <span>www.website.com</span>
      </li>
    </ul>

    <div class="address">
      <svg class="icon" viewBox="0 0 24 24" aria-hidden="true"><path d="M12 2a7 7 0 0 0-7 7c0 5 7 13 7 13s7-8 7-13a7 7 0 0 0-7-7zm0 9.5a2.5 2.5 0 1 1 0-5 2.5 2.5 0 0 1 0 5z"/></svg>
      <span>421, Address line goes here<br>45452, Country name</span>
    </div>
  </section>
</body>
</html>
```